Pruitt Denatl Laboratory nees a window design

We want to make a window cover 8 feet wide and 6 feet tall to advertise our dental lab with all the products we produce<br/>: Digital Cad/Cam<br/>: Implants<br/>: Dentures<br/>: Cast Partials <br/>: Orthodontic appliances<br/><br/> and it has to include a service we provide for a denturist on site by appointment only.<br/><br/>Please use the sample logo below our colours are white backround and blue letters

Font styles to use
Script

Colors
ffffff
0355a3

Requirements
Nice to have
• a picture of a teddy bear on a dental chair, or some dental work particularly bridge work since our moto is Building bridges since 1976
Should not have
• real people

```html
<!DOCTYPE html>
<html lang="en">
<head>
<meta charset="utf-8">
<title>Pruitt Dental Laboratory – Window Banner</title>
<link rel="stylesheet" href="https://fonts.googleapis.com/css2?family=EB+Garamond:ital,wght@0,600;0,700;1,500&display=swap">
<style>
  :root {
    --page-bg: #221f20;
    --brand-blue: #0355a3;
    --name-blue: #1a8ccf;
    --sky: #a9d9ec;
    --white: #ffffff;
  }
  html, body {
    margin: 0;
    padding: 0;
    width: 1200px;
    height: 1200px;
    overflow: hidden;
    background: var(--page-bg);
  }
  .banner {
    position: absolute;
    left: 54px;
    top: 327px;
    width: 1092px;
    height: 546px;
    overflow: hidden;
    background:
      radial-gradient(ellipse 420px 360px at 330px 300px, var(--white) 0%, #e4f2f9 45%, rgba(169,217,236,0) 100%),
      var(--sky);
    font-family: "EB Garamond", Georgia, serif;
  }
  .top-band {
    position: absolute;
    left: 0; top: 0;
    width: 100%;
    height: 19px;
    background: var(--brand-blue);
  }
  .brand {
    position: absolute;
    left: 60px;
    top: 64px;
    width: 620px;
    text-align: center;
    color: var(--name-blue);
    font-weight: 600;
  }
  .brand-name {
    display: block;
    font-size: 96px;
    line-height: 86px;
    letter-spacing: 2px;
  }
  .brand-sub {
    display: block;
    font-size: 34px;
    line-height: 44px;
    letter-spacing: 4px;
  }
  .services {
    position: absolute;
    left: 40px;
    top: 256px;
    width: 620px;
    margin: 0;
    text-align: center;
    color: var(--brand-blue);
    font-weight: 700;
    font-size: 44px;
    line-height: 57px;
    letter-spacing: -1px;
  }
  .services span { display: block; }
  .tooth-art {
    position: absolute;
    left: 743px;
    top: 70px;
    width: 289px;
    height: 419px;
    border-radius: 120px 120px 60px 60px;
    background: radial-gradient(ellipse at 45% 35%, #ffffff 0%, #eeeeee 50%, #cfcfcf 100%);
  }
  .appointment-band {
    position: absolute;
    left: 0;
    top: 476px;
    width: 717px;
    height: 70px;
    background: var(--brand-blue);
    clip-path: polygon(0 0, 655px 0, 717px 100%, 0 100%);
  }
  .appointment-text {
    position: absolute;
    left: 28px;
    top: 10px;
    margin: 0;
    color: var(--white);
    font-style: italic;
    font-weight: 500;
    font-size: 36px;
    line-height: 48px;
    letter-spacing: -0.5px;
    white-space: nowrap;
    transform: scaleX(0.78);
    transform-origin: left center;
  }
</style>
</head>
<body>
  <section class="banner">
    <div class="top-band"></div>

    <div class="brand">
      <span class="brand-name">PRUITT</span>
      <span class="brand-sub">DENTAL LABORATORY</span>
    </div>

    <p class="services">
      <span>DIGITAL CAD | IMPLANTS |</span>
      <span>DENTURES | CAST PARTIALS |</span>
      <span>ORTHODONTIC APPLIANCES</span>
    </p>

    <div class="tooth-art" role="img" aria-label="Glossy white 3D molar tooth illustration"></div>

    <div class="appointment-band">
      <p class="appointment-text">DENTURIST : ON SITE BY APPOINTMENT ONLY</p>
    </div>
  </section>
</body>
</html>
```